Therapy and counselling practice needs a compelling double-sided promotional flyer

We need someone to design a highly engaging, easy to read, revenue generating promotional flyer that we can give to potential new clients. I have attached the content I need you to include, as well as the professional photo of myself and the company logo. Please use a colour scheme which matches the colours used in my logo. Our website is www.velmira.com.au for reference to our practice. Need something that looks really modern and eye catching and positions the content in a way which isn't just like a jazzed up Word document.
Updates

Please also feel free to use additional images as you deem appropriate, relating to therapy / counselling with clients. See my website for examples - velmira.com.au

```html
<!DOCTYPE html>
<html lang="en">
<head>
<meta charset="utf-8">
<title>Velmira Health Services – Counselling Flyer</title>
<link rel="stylesheet" href="https://fonts.googleapis.com/css2?family=Montserrat:wght@400;500;600;700;800;900&family=Quicksand:wght@500;600;700&family=Dancing+Script:wght@600&display=swap">
<style>
:root{
  --red:#dc1c23;
  --yellow:#ffd200;
  --black:#0d0d0d;
  --ink:#222;
  --grey:#555;
  --white:#fff;
}
*{margin:0;padding:0;box-sizing:border-box}
html,body{width:1200px;height:2700px;overflow:hidden}
body{position:relative;background:var(--white);font-family:'Montserrat',sans-serif;color:var(--ink)}
.board-band{position:absolute;left:0;top:0;width:470px;height:2700px;background:var(--red)}
.side-label{position:absolute;left:160px;color:var(--white);font:700 22px 'Montserrat',sans-serif;letter-spacing:1px}
.page{position:absolute;left:154px;width:896px;background:var(--white);box-shadow:0 6px 24px rgba(0,0,0,.25);overflow:hidden}
.page--front{top:120px;height:1157px}
.page--back{top:1420px;height:1155px}
.abs{position:absolute}
.headline{left:55px;top:56px;font-weight:900;font-size:48px;line-height:42px;letter-spacing:-.5px}
.headline .hl-red{color:var(--red)}
.headline .hl-black{color:var(--black)}
.logo-card{left:545px;top:43px;width:290px;height:160px;background:var(--white);border-radius:30px;box-shadow:0 4px 14px rgba(0,0,0,.25);display:flex;align-items:center;justify-content:center;gap:10px}
.brand-dot{width:18px;height:18px;border-radius:50%;background:var(--red)}
.brand-name{font-weight:800;font-size:46px;color:var(--black);letter-spacing:-1px}
.photo{background:linear-gradient(135deg,#c9c5c0,#8a7b6d)}
.intro{left:60px;top:300px;width:360px;color:var(--white);font-size:12.5px;line-height:16px}
.emblem{border-radius:50%;background:var(--yellow);border:8px solid var(--white)}
.tab{left:0;width:896px}
.tab-title{position:absolute;left:0;width:896px;text-align:center;color:var(--white);font:700 25px 'Quicksand',sans-serif;white-space:nowrap}
.pill{position:absolute;height:30px;background:var(--yellow);border-radius:15px;padding-left:40px;display:flex;align-items:center;font-weight:800;font-size:16px;color:var(--black);white-space:nowrap}
.pill::before{content:"";position:absolute;left:-4px;top:-2px;width:34px;height:34px;border-radius:50%;background:var(--white);border:4px solid var(--red)}
.pill--sm{font-size:13.5px}
.body{font-size:11.5px;line-height:14px;color:var(--grey)}
.body--lg{font-size:12.5px;line-height:16px}
.ticks{list-style:none}
.ticks li{position:relative;padding-left:21px;font-size:11.5px;line-height:12.5px;font-weight:600;color:var(--ink)}
.ticks li::before{content:"";position:absolute;left:2px;top:2px;width:9px;height:9px;border:1.5px solid var(--red);border-radius:50%}
.ticks li::after{content:"";position:absolute;left:5.5px;top:4px;width:2.5px;height:4px;border:solid var(--red);border-width:0 1.5px 1.5px 0;transform:rotate(45deg)}
.ticks--lg li{font-size:13px;line-height:16px;font-weight:500}
.technique{font-size:11.5px;line-height:14px;font-weight:600;color:var(--ink)}
.technique b{color:var(--red);font-weight:500}
.red-note{color:var(--red);font-weight:600;font-size:13px}
.divider-line{background:var(--black)}
.cta-title{left:359px;top:626px;font:700 29px 'Quicksand',sans-serif;color:var(--black)}
.cta-text{left:359px;top:668px;width:480px;font:500 16.5px/20px 'Quicksand',sans-serif;color:#333}
.cta-red{left:359px;top:739px;font:600 21px 'Quicksand',sans-serif;color:var(--red)}
.contact-script{left:78px;top:800px;font:600 48px 'Dancing Script',cursive;color:var(--red)}
.contact-name{left:76px;top:862px;font:700 48px 'Quicksand',sans-serif;color:#333}
.contact-role{left:78px;top:922px;font:600 22px 'Quicksand',sans-serif;color:#555}
.schedule{left:51px;top:974px;width:520px;height:49px;background:var(--red);border-radius:25px;color:var(--white);font:600 22px 'Montserrat',sans-serif;padding-left:22px;display:flex;align-items:center}
.contact-row{left:62px;top:1046px;display:flex;align-items:center;gap:12px;font:700 18px 'Quicksand',sans-serif;color:var(--black)}
.icon-dot{width:26px;height:26px;border-radius:50%;background:var(--yellow);display:flex;align-items:center;justify-content:center}
.site{left:65px;top:1093px;color:var(--white);font:700 29px 'Quicksand',sans-serif;letter-spacing:1.5px}
</style>
</head>
<body>
<div class="board-band"></div>

<!-- FRONT -->
<section class="page page--front">
  <svg class="abs" style="left:0;top:0" width="896" height="440" viewBox="0 0 896 440">
    <path d="M0 264 H640 C700 264 735 250 752 210 L848 0 H896 V430 H0 Z" fill="var(--red)"/>
    <path d="M640 254 C698 254 728 240 745 202 L838 0" fill="none" stroke="var(--yellow)" stroke-width="10"/>
  </svg>
  <h1 class="abs headline">
    <span class="hl-red">RECLAIM YOUR<br>WELL-BEING</span><br>
    <span class="hl-black">WITH EXPERT<br>COUNSELLING</span>
  </h1>
  <div class="abs logo-card"><span class="brand-dot"></span><span class="brand-name">Velmira</span></div>
  <div class="abs photo" style="left:480px;top:190px;width:416px;height:233px;background:linear-gradient(180deg,rgba(255,255,255,0) 0%,#a78a6a 70%,#6e4e34 100%)" role="img" aria-label="Counsellor taking notes while a client talks, both seated in wooden armchairs"></div>
  <p class="abs intro">Life’s challenges and traumas can sometimes feel overwhelming. At Velmira Health Services, we believe in your potential to overcome obstacles and lead a meaningful, fulfilling life. As a highly qualified therapist and counsellor, my name is Lukas Brenner, and I’m here to support you on your journey every step of the way.</p>
  <div class="abs emblem" style="left:426px;top:327px;width:84px;height:84px"></div>

  <svg class="abs tab" style="top:423px" width="896" height="62" viewBox="0 0 896 62">
    <rect x="0" y="0" width="896" height="12" fill="var(--black)"/>
    <path d="M141 0 H750 C720 0 715 59 680 59 H211 C176 59 171 0 141 0 Z" fill="var(--black)"/>
  </svg>
  <h2 class="tab-title" style="top:438px">Why Choose Me as Your Therapist?</h2>

  <div class="abs divider-line" style="left:449px;top:521px;width:5px;height:614px"></div>

  <div class="pill" style="left:53px;top:507px;width:281px">Comprehensive Expertise</div>
  <p class="abs body" style="left:53px;top:548px;width:345px">I bring a unique combination of skills and experience to my counselling practice, blending years of corporate leadership with a deep understanding of mental health. My background includes:</p>
  <ul class="abs ticks" style="left:53px;top:612px;width:310px">
    <li>Over a decade in corporate roles, specialising in leadership development, workplace culture, and HR strategy.</li>
    <li style="margin-top:12px">Consulting experience with small to medium-sized enterprises, focusing on leadership coaching and employee engagement.</li>
  </ul>
  <p class="abs body" style="left:53px;top:712px;width:345px">This foundation allows me to offer unique insights into the challenges faced by professionals and leaders, including work-related stress, burnout, and interpersonal dynamics.</p>
  <div class="abs photo" style="left:62px;top:768px;width:173px;height:108px;border-radius:54px 0 0 54px" role="img" aria-label="Family of three sitting together on a sofa"></div>
  <div class="abs photo" style="left:242px;top:768px;width:158px;height:108px" role="img" aria-label="Couple in a counselling session, seen across the room"></div>

  <div class="pill" style="left:53px;top:888px;width:363px">Specialised Therapeutic Techniques</div>
  <p class="abs body" style="left:58px;top:929px;width:300px">At Velmira Health Services, I use evidence-based approaches tailored to your individual needs:</p>
  <p class="abs technique" style="left:60px;top:972px;width:310px"><b>Cognitive Behavioural Therapy (CBT):</b><br>Helping you identify and reframe unhelpful thought patterns.</p>
  <p class="abs technique" style="left:60px;top:1022px;width:320px"><b>Acceptance and Commitment Therapy (ACT):</b> Supporting you to embrace challenges while staying committed to your values.</p>
  <p class="abs technique" style="left:60px;top:1074px;width:310px"><b>Motivational Questioning:</b><br>Encouraging meaningful change by exploring your strengths and aspirations.</p>

  <div class="pill" style="left:498px;top:508px;width:275px">Extensive Qualifications</div>
  <p class="abs body" style="left:504px;top:549px;width:320px">I bring a solid foundation of academic and professional experience, including:</p>
  <ul class="abs ticks" style="left:502px;top:589px;width:320px">
    <li>Diploma of Counselling (Southern Institute of Counselling Studies).</li>
    <li style="margin-top:9px">Certified Adolescent Counsellor (Eastbay University).</li>
    <li style="margin-top:9px">Postgraduate qualifications in Human Resource Management.</li>
  </ul>
  <div class="abs photo" style="left:498px;top:689px;width:159px;height:110px" role="img" aria-label="Older couple speaking with a counsellor"></div>
  <div class="abs photo" style="left:664px;top:689px;width:172px;height:110px;border-radius:0 55px 55px 0;background:linear-gradient(135deg,#cfc8bf,#3a3a3a)" role="img" aria-label="Man in a suit listening during a session"></div>

  <div class="pill" style="left:498px;top:816px;width:264px">Trauma-Informed Care</div>
  <p class="abs body" style="left:502px;top:858px;width:350px">As a trauma-informed counsellor, I understand the profound impact that trauma can have on mental, emotional, and physical well-being. Trauma-informed care means recognising the prevalence of trauma, understanding its effects, and creating a safe, supportive environment for healing.</p>
  <p class="abs red-note" style="left:500px;top:944px">This approach benefits clients by:</p>
  <ul class="abs ticks" style="left:502px;top:969px;width:340px">
    <li>Ensuring that therapy is sensitive to past experiences and avoids re-traumatisation.</li>
    <li style="margin-top:10px">Helping clients build trust and safety in the therapeutic relationship.</li>
    <li style="margin-top:10px">Empowering individuals to regain control, develop resilience, and move forward with confidence.</li>
  </ul>
  <p class="abs body" style="left:500px;top:1074px;width:320px">Whether you’re dealing with childhood trauma, grief, or life-altering events, I’m here to help you navigate your journey towards healing and recovery.</p>

  <div class="abs" style="left:0;top:1135px;width:896px;height:8px;background:var(--black)"></div>
  <div class="abs" style="left:0;top:1143px;width:896px;height:14px;background:var(--red)"></div>
</section>
<div class="side-label" style="top:1300px">FRONT</div>

<!-- BACK -->
<section class="page page--back">
  <svg class="abs tab" style="top:0;height:86px" width="896" height="86" viewBox="0 0 896 86">
    <rect x="0" y="0" width="896" height="38" fill="var(--black)"/>
    <path d="M141 38 H750 C720 38 715 85 680 85 H211 C176 85 171 38 141 38 Z" fill="var(--black)"/>
  </svg>
  <h2 class="tab-title" style="top:30px">Why Choose Me as Your Therapist?</h2>

  <div class="pill" style="left:46px;top:120px;width:336px">A Unique Counselling Approach</div>
  <p class="abs body body--lg" style="left:44px;top:164px;width:400px">I take a person-centred approach to therapy, creating a safe, confidential, and supportive environment where you can openly explore your concerns. My goal is to empower you to:</p>
  <ul class="abs ticks ticks--lg" style="left:454px;top:129px;width:180px">
    <li>Navigate and heal from trauma.</li>
    <li style="margin-top:16px">Develop resilience and coping strategies.</li>
  </ul>
  <ul class="abs ticks ticks--lg" style="left:648px;top:129px;width:200px">
    <li>Improve relationships and communication.</li>
    <li style="margin-top:16px">Achieve personal growth and fulfilment.</li>
  </ul>
  <p class="abs body body--lg" style="left:42px;top:238px;width:820px">Whether you are seeking support as an individual or as a couple, I am experienced in addressing a variety of challenges, including relationship dynamics, communication breakdowns, and emotional well-being. Together, we will work towards fostering stronger connections and healthier relationships.</p>

  <div class="abs photo" style="left:44px;top:300px;width:198px;height:124px;border-radius:62px 0 0 62px" role="img" aria-label="Group counselling session with several men"></div>
  <div class="abs photo" style="left:251px;top:300px;width:190px;height:124px" role="img" aria-label="Young woman listening in a counselling room"></div>
  <div class="abs photo" style="left:455px;top:300px;width:190px;height:124px" role="img" aria-label="Support group members sitting in a circle"></div>
  <div class="abs photo" style="left:653px;top:300px;width:199px;height:124px;border-radius:0 62px 62px 0" role="img" aria-label="Family with a child speaking with a counsellor"></div>
  <div class="abs emblem" style="left:390px;top:306px;width:114px;height:114px;border-color:var(--red)"></div>

  <div class="pill pill--sm" style="left:46px;top:453px;width:351px">Modern and Trusted Counselling Practice</div>
  <div class="pill pill--sm" style="left:474px;top:455px;width:349px">Online Counselling for Your Convenience</div>
  <p class="abs body body--lg" style="left:48px;top:497px;width:375px">Based in Seaview Victoria, Velmira Health Services is a full-service counselling practice dedicated to supporting individuals across various life stages. Our focus is on delivering impactful results through tailored, individualised therapy that addresses your unique challenges.</p>
  <p class="abs body body--lg" style="left:475px;top:497px;width:365px">All sessions are conducted online via Meetly, enabling me to reach a broader audience nationally while keeping sessions cost-effective. This flexible approach allows you to access high-quality counselling from the comfort of your own home, wherever you are located.</p>

  <div class="abs" style="left:48px;top:604px;width:792px;height:1.5px;background:#999"></div>

  <div class="abs" style="left:92px;top:660px;display:flex;align-items:center;gap:12px">
    <span class="brand-dot" style="width:22px;height:22px"></span>
    <span class="brand-name" style="font-size:54px">Velmira</span>
  </div>

  <h3 class="abs cta-title">Take the First Step Today</h3>
  <p class="abs cta-text">Your journey to well-being starts with a conversation. Whether you’re seeking to overcome trauma, manage mental health challenges, or navigate life’s transitions,</p>
  <p class="abs cta-red">I’m here to support you.</p>

  <p class="abs contact-script">Contact</p>
  <p class="abs contact-name">Lukas Brenner</p>
  <p class="abs contact-role">Practice Owner and Lead Therapist</p>
  <div class="abs schedule">TO SCHEDULE YOUR CONSULTATION</div>

  <div class="abs photo" style="left:529px;top:757px;width:367px;height:383px;background:linear-gradient(180deg,#f4f4f4 0%,#c8b9ad 35%,#3b4452 65%,#262d38 100%);border-radius:180px 180px 0 0" role="img" aria-label="Portrait of the lead therapist in a dark suit and blue tie"></div>

  <div class="abs contact-row">
    <span class="icon-dot"><svg width="14" height="14" viewBox="0 0 24 24"><path d="M6.6 10.8a15 15 0 0 0 6.6 6.6l2.2-2.2a1 1 0 0 1 1-.25 11.4 11.4 0 0 0 3.6.57 1 1 0 0 1 1 1V20a1 1 0 0 1-1 1A17 17 0 0 1 3 4a1 1 0 0 1 1-1h3.5a1 1 0 0 1 1 1c0 1.25.2 2.45.57 3.57a1 1 0 0 1-.25 1Z" fill="var(--black)"/></svg></span>
    <span>(03) 9000 4821</span>
    <span class="icon-dot" style="margin-left:6px"><svg width="14" height="12" viewBox="0 0 24 18"><rect x="1" y="1" width="22" height="16" rx="2" fill="var(--black)"/><path d="M2 2l10 8 10-8" fill="none" stroke="var(--yellow)" stroke-width="2"/></svg></span>
    <span>lukas@velmira.com.au</span>
  </div>

  <svg class="abs" style="left:0;top:1086px" width="896" height="69" viewBox="0 0 896 69">
    <path d="M0 0 H410 C440 0 450 46 480 46 H896 V54 H0 Z" fill="var(--black)"/>
    <rect x="0" y="54" width="896" height="15" fill="var(--red)"/>
  </svg>
  <p class="abs site">www.velmira.com.au</p>
</section>
<div class="side-label" style="top:2597px">BACK</div>
</body>
</html>
```